Templates for Construction Company

We are looking to have templates prepared for all aspects of our letter sending. Using our brand design. with similar layouts that look the same.

Letterheads design & Email signatures

We use letter heads for - quotes, contract correspondence, variations, formal letters, invitations

Target Market(s)

Clients documents sent in emails

Industry/Entity Type

Construction

Font styles to use
Serif
Sans Serif

Colors
0054AA
0677BA
7BADD7
CADEEF
E8F1F8

Requirements
Must have
• Easy to read, water marks on page
Nice to have
• Different options for different letters

```html
<!DOCTYPE html>
<html lang="en">
<head>
<meta charset="utf-8">
<title>Ridgeline Construction Group – Stationery Set</title>
<link href="https://fonts.googleapis.com/css2?family=Montserrat:wght@400;600;700;800&family=Questrial&display=swap" rel="stylesheet">
<style>
  :root {
    --board: #7f7e7f;
    --paper: #f3f7fd;
    --brand-blue: #5a8ac6;
    --ink-dark: #555555;
    --ink-body: #6a6a6a;
    --watermark: #e1e8f2;
    --white: #ffffff;
    --label: #1f1f1f;
  }
  * { margin: 0; padding: 0; box-sizing: border-box; }
  html, body { width: 874px; height: 1200px; overflow: hidden; }
  body {
    position: relative;
    background: var(--board);
    font-family: "Questrial", "Montserrat", sans-serif;
    color: var(--ink-dark);
  }
  .sheet {
    position: absolute;
    width: 349px;
    height: 493px;
    background: var(--paper);
    overflow: hidden;
    box-shadow: 0 1px 4px rgba(0,0,0,0.25);
  }
  .sheet--front { left: 70px; top: 81px; }
  .sheet--letter { left: 450px; top: 81px; }
  .sheet--continuation { left: 70px; top: 613px; }
  .sheet--back { left: 450px; top: 613px; background: var(--brand-blue); }

  .sheet-label {
    position: absolute;
    width: 349px;
    text-align: center;
    font-family: "Montserrat", sans-serif;
    font-weight: 600;
    font-size: 10px;
    letter-spacing: 1.2px;
    color: var(--label);
  }
  .sheet-label--front { left: 70px; top: 587px; }
  .sheet-label--letter { left: 450px; top: 587px; }
  .sheet-label--continuation { left: 70px; top: 1120px; }
  .sheet-label--back { left: 450px; top: 1120px; }

  /* brand name block */
  .brand {
    position: absolute;
    display: flex;
    align-items: center;
    gap: 6px;
    font-family: "Montserrat", sans-serif;
    font-weight: 700;
    color: var(--brand-blue);
  }
  .brand-square { background: var(--brand-blue); flex: none; }
  .brand-name { line-height: 1.05; }

  .brand--cover { left: 0; right: 0; top: 60px; justify-content: center; font-size: 24px; }
  .brand--cover .brand-square { width: 14px; height: 14px; }
  .brand--letter { left: 33px; top: 33px; font-size: 14px; }
  .brand--letter .brand-square { width: 9px; height: 9px; }

  /* front cover */
  .cover-title {
    position: absolute; left: 0; right: 0; top: 202px; text-align: center;
    font-family: "Montserrat", sans-serif; font-weight: 800;
    font-size: 26px; color: var(--brand-blue); letter-spacing: 0.2px;
  }
  .cover-subtitle {
    position: absolute; left: 0; right: 0; top: 231px; text-align: center;
    font-family: "Montserrat", sans-serif; font-weight: 700;
    font-size: 22px; color: var(--ink-dark);
  }
  .cover-intro {
    position: absolute; left: 40px; right: 40px; top: 257px; text-align: center;
    font-size: 8px; line-height: 10px; color: var(--ink-dark);
  }
  .cover-band {
    position: absolute; left: 0; right: 0; top: 416px; height: 57px;
    background: var(--brand-blue); color: var(--white); text-align: center;
  }
  .cover-name {
    margin-top: 4px;
    font-family: "Montserrat", sans-serif; font-weight: 800; font-size: 15px;
  }
  .cover-role {
    font-family: "Montserrat", sans-serif; font-weight: 700; font-size: 8.5px; margin-top: 1px;
  }
  .cover-date { font-family: "Montserrat", sans-serif; font-size: 10.5px; margin-top: 4px; }
  .cover-date sup { font-size: 6px; }

  /* letterhead */
  .contact-block {
    position: absolute; left: 221px; top: 36px;
    font-family: "Montserrat", sans-serif; font-size: 6.3px; line-height: 8.4px; color: var(--ink-dark);
  }
  .contact-line { display: flex; align-items: center; gap: 3px; }
  .contact-line svg { width: 6px; height: 6px; flex: none; }
  .contact-icon { fill: var(--brand-blue); }

  .watermark {
    position: absolute;
    font-family: "Montserrat", sans-serif; font-weight: 700;
    color: var(--watermark);
    white-space: nowrap;
  }
  .watermark--letter { left: 110px; top: 240px; font-size: 46px; }
  .watermark--continuation { left: 0; right: 0; top: 220px; text-align: center; font-size: 58px; }

  .letter {
    position: absolute; left: 33px; top: 157px; width: 284px;
    color: var(--ink-body);
  }
  .letter-greeting { font-size: 8.5px; color: var(--ink-dark); margin-bottom: 15px; }
  .letter-body p { font-size: 5.1px; line-height: 7.4px; margin-bottom: 6px; text-align: justify; }
  .letter-closing { font-size: 5.1px; margin-top: 6px; }
  .signature { display: block; width: 40px; height: 8px; margin-top: 14px; background: #cfd6df; }

  .footer-band {
    position: absolute; left: 0; right: 0; top: 465px; height: 11px;
    background: var(--brand-blue); color: var(--white);
    font-family: "Montserrat", sans-serif; font-size: 5.6px; letter-spacing: 1.3px;
    text-align: center; line-height: 11px;
  }

  /* back cover */
  .back-mark {
    position: absolute; left: 0; right: 0; top: 205px; text-align: center;
    font-family: "Montserrat", sans-serif; font-weight: 700; font-size: 40px; color: var(--white);
  }
  .back-contact {
    position: absolute; left: 0; right: 0; top: 434px; text-align: center;
    font-family: "Montserrat", sans-serif; font-size: 8px; line-height: 11px; color: var(--white);
  }
  .back-web { font-weight: 700; }
</style>
</head>
<body>

  <!-- Front cover -->
  <section class="sheet sheet--front">
    <div class="brand brand--cover">
      <span class="brand-square"></span>
      <span class="brand-name">Ridgeline<br>Construction Group</span>
    </div>
    <h1 class="cover-title">TITLE GOES HERE</h1>
    <h2 class="cover-subtitle">Subtitle Goes Here</h2>
    <p class="cover-intro">Faucibus, ipsum nec aliquet viverra, leo mauris condimentligula,<br>sit amet sagittis enim ligula quis arcu.</p>
    <div class="cover-band">
      <div class="cover-name">DANIEL HARPER</div>
      <div class="cover-role">PRESIDENT</div>
      <div class="cover-date">18<sup>TH</sup> May 2021</div>
    </div>
  </section>
  <div class="sheet-label sheet-label--front">FRONT</div>

  <!-- Letterhead page -->
  <section class="sheet sheet--letter">
    <div class="watermark watermark--letter">Ridgeline</div>
    <div class="brand brand--letter">
      <span class="brand-square"></span>
      <span class="brand-name">Ridgeline<br>Construction Group</span>
    </div>
    <address class="contact-block" style="font-style:normal">
      <div>412 Harbor Ridge Road</div>
      <div>Juneau, Alaska 99801</div>
      <div class="contact-line">
        <svg viewBox="0 0 10 10"><rect class="contact-icon" x="2.5" y="0.5" width="5" height="9" rx="1"/></svg>555-210-4830
      </div>
      <div class="contact-line">
        <svg viewBox="0 0 10 10"><rect class="contact-icon" x="1" y="3" width="8" height="5" rx="1"/><rect class="contact-icon" x="3" y="1" width="4" height="2"/></svg>555-318-7264
      </div>
      <div class="contact-line">
        <svg viewBox="0 0 10 10"><path class="contact-icon" d="M1 2h8v6H1z M1 2l4 3.5L9 2" stroke="#fff" stroke-width="0.6"/></svg>name@ridgelineconstruction.com
      </div>
    </address>
    <article class="letter">
      <p class="letter-greeting">Dear Mr. Harper,</p>
      <div class="letter-body">
        <p>Thank you for meeting with our team last week to review the plans for your new office building. We have prepared a full quote covering site preparation, foundations, framing, roofing and interior finishing. Each stage lists labour, materials and expected time so you can compare every part of the work with ease and plan your budget with confidence.</p>
        <p>Our crew can begin work on site within three weeks of signing the contract. We will keep you informed with a short written report at the end of each week, and our project manager will be available by phone for any questions. Any change to the scope will be shared as a written variation before work goes ahead.</p>
        <p>All materials are sourced from trusted local suppliers and meet current building codes. Our team holds full insurance and safety training, and every site is inspected daily. We clean up at the close of each day so the area stays safe for staff, visitors and neighbours. Warranty terms for all finished work are included in the attached pages.</p>
        <p>Please review the quote and let us know if you would like any changes. We look forward to working with you and building a space your business will be proud to call home.</p>
      </div>
      <p class="letter-closing">Sincerely,</p>
      <span class="signature" role="img" aria-label="Handwritten signature"></span>
    </article>
    <div class="footer-band">www.ridgelineconstruction.com</div>
  </section>
  <div class="sheet-label sheet-label--letter">PAGE 1</div>

  <!-- Continuation page -->
  <section class="sheet sheet--continuation">
    <div class="watermark watermark--continuation">Ridgeline</div>
    <div class="footer-band">www.ridgelineconstruction.com</div>
  </section>
  <div class="sheet-label sheet-label--continuation">PAGE2</div>

  <!-- Back cover -->
  <section class="sheet sheet--back">
    <div class="back-mark">Ridgeline</div>
    <div class="back-contact">
      <div>412 Harbor Ridge Road, Juneau, Alaska 99801</div>
      <div>P. 555-210-4830 M. 555-318-7264 E. name@ridgelineconstruction.com</div>
      <div class="back-web">www.ridgelineconstruction.com</div>
    </div>
  </section>
  <div class="sheet-label sheet-label--back">BACK</div>

</body>
</html>
```